Flyer Design Project

I provide workshops for teachers, students and parents on organization - specifically laying out 3 goals, their accompanying activities and actions in 3 three hour sessions.

Please go to my website to see my brain logo. I need a flyer with the information typed below. The information may be changed and/or added to in way you see fit to better communicate the organizational intent.This is not for speech therapy clients, rather, it is for any and everyone who needs help writing out goals.

I would like the design of the flyer to reflect the concept of organization in a unique way.

http://themindcraftstudyhouse.com/wp-content/uploads/2012/02/websitelogo2.jpg

ORGANIZATION

Write out your goals for the year.

How to organize your life in 3 easy steps.
Have fun organizing your life and plans.
Join a group of people dedicated to organizing all areas of life.
Complete your tasks in a fast, fun game format.
Walk away with your major goals broken down into their component parts and organize on a yearly calendar.
Three 3 hour days spent in making your life happier, less stressed and with realistic picture of what needs to be accomplished.
more effective in everything I do.
Being organized helps free our minds, enjoy relationships more, feel happier, and have greater meaning in life.

You will walk away with detailed plans for 2013.

COST: $600 for all three days.

WHO: Led by Maren Holtby, Cognitive Speech Therapist
WHERE: 4971 E Pruett Ave
Kennewick, WA 99336
509-218-3907

Requirements
Must have
• My logo from my website. A unique organized appearance.

```html
<!DOCTYPE html>
<html lang="en">
<head>
<meta charset="utf-8">
<title>Organization Workshop Flyer</title>
<link rel="stylesheet" href="https://fonts.googleapis.com/css2?family=EB+Garamond:wght@600;700&family=Nunito:wght@700;800&display=swap">
<style>
  :root {
    --page: #e7e4df;
    --cream: #fbf8e4;
    --white: #ffffff;
    --navy: #0d4f94;
    --navy-deep: #0a3f78;
    --orange: #e8821c;
    --green: #8cc63f;
    --ink: #151515;
    --brand-blue: #1f3f9a;
    --badge: #ffd21a;
    --badge-edge: #f5b800;
    --serif: "EB Garamond", Georgia, serif;
    --round: "Nunito", Arial, sans-serif;
  }
  * { box-sizing: border-box; margin: 0; padding: 0; }
  html, body { width: 1200px; height: 900px; overflow: hidden; background: var(--page); }
  .flyer {
    position: absolute; left: 210px; top: 110px; width: 840px; height: 593px;
    background: var(--white); overflow: hidden;
    box-shadow: 0 6px 18px rgba(0,0,0,.25);
  }
  .flyer__header {
    position: absolute; left: 0; top: 0; width: 840px; height: 80px;
    background: linear-gradient(180deg, #ffffff 0%, var(--cream) 100%);
    border-bottom: 3px solid var(--navy);
  }
  .brand { position: absolute; left: 18px; top: 20px; display: flex; align-items: center; gap: 12px; }
  .brand__dot { width: 40px; height: 40px; border-radius: 50%; background: var(--navy-deep); }
  .brand__name { font-family: var(--serif); font-weight: 700; font-size: 25px; color: var(--brand-blue); }

  .swoosh-area { position: absolute; }
  .swoosh-area--header {
    left: 450px; top: 4px; width: 390px; height: 72px;
    background: linear-gradient(170deg, rgba(140,198,63,0) 20%, rgba(140,198,63,.35) 55%, rgba(232,130,28,.35) 80%, rgba(232,130,28,0) 100%);
  }
  .swoosh-area--side {
    left: 0; top: 86px; width: 215px; height: 56px;
    background: linear-gradient(175deg, rgba(232,130,28,.45) 0%, rgba(232,130,28,.3) 40%, rgba(140,198,63,.4) 70%, rgba(140,198,63,0) 100%);
  }

  .watermark { position: absolute; border-radius: 50%; }
  .watermark--side {
    left: 120px; top: 200px; width: 90px; height: 150px;
    background: radial-gradient(ellipse at center, rgba(240,230,150,.45) 0%, rgba(240,230,150,0) 70%);
  }
  .watermark--panel {
    left: 60px; top: 150px; width: 290px; height: 320px;
    background: radial-gradient(circle at center, rgba(60,130,200,.35) 0%, rgba(60,130,200,.15) 45%, rgba(60,130,200,0) 70%);
  }

  .details {
    position: absolute; left: 16px; top: 150px; width: 195px;
    font-family: var(--serif); font-weight: 700; font-size: 15px; line-height: 26px; color: var(--ink);
  }
  .details__block { margin-bottom: 25px; }

  .panel {
    position: absolute; left: 215px; top: 85px; width: 625px; height: 430px;
    background: var(--navy); overflow: hidden;
  }
  .panel__title {
    position: absolute; left: 167px; top: 35px;
    font-family: var(--serif); font-weight: 700; font-size: 24px; letter-spacing: .5px; color: var(--white);
  }
  .panel__art {
    position: absolute; left: 395px; top: 5px; width: 225px; height: 150px; border-radius: 30px;
    background: radial-gradient(ellipse at 45% 40%, rgba(226,162,58,.9) 0%, rgba(201,134,42,.6) 40%, rgba(127,169,230,.45) 70%, rgba(127,169,230,0) 100%);
  }
  .benefits { list-style: none; position: absolute; left: 36px; top: 91px; width: 525px; }
  .benefits li {
    position: relative; padding-left: 38px; margin-bottom: 16px;
    font-family: var(--round); font-weight: 700; font-size: 13px; line-height: 17px; letter-spacing: 1.1px; color: var(--white);
  }
  .benefits li:nth-child(6), .benefits li:nth-child(7) { margin-bottom: 15px; }
  .gear { position: absolute; left: 0; top: 50%; width: 26px; height: 26px; margin-top: -11px; }
  .benefits li:nth-child(-n+5) .gear { margin-top: -12px; }

  .band {
    position: absolute; left: 0; top: 515px; width: 840px; height: 78px; background: var(--orange);
    border-bottom: 11px solid var(--navy);
  }
  .band__text {
    position: absolute; left: 168px; top: 22px;
    font-family: var(--round); font-weight: 800; font-size: 19px; letter-spacing: 1.8px; color: var(--white);
  }
  .price-badge { position: absolute; left: 20px; top: 418px; width: 160px; height: 150px; }
  .price-badge__text {
    position: absolute; left: 0; top: 0; width: 160px; height: 150px;
    display: flex; align-items: center; justify-content: center; text-align: center;
    transform: rotate(-22deg);
    font-family: var(--round); font-weight: 800; font-size: 18px; line-height: 20px; letter-spacing: 1.5px; color: var(--ink);
  }
</style>
</head>
<body>
<svg width="0" height="0" style="position:absolute" aria-hidden="true">
  <symbol id="gear-icon" viewBox="0 0 26 26">
    <circle cx="13" cy="13" r="10" fill="none" stroke="var(--white)" stroke-width="4" stroke-dasharray="3.4 2.9"/>
    <circle cx="13" cy="13" r="9" fill="var(--badge)" stroke="var(--white)" stroke-width="1.5"/>
    <circle cx="13" cy="13" r="3" fill="var(--navy)"/>
  </symbol>
</svg>
<main class="flyer">
  <header class="flyer__header">
    <div class="brand">
      <span class="brand__dot"></span>
      <span class="brand__name">The Mindcraft Study House</span>
    </div>
  </header>
  <div class="swoosh-area swoosh-area--header" role="img" aria-label="Decorative orange and green curved swooshes"></div>
  <div class="swoosh-area swoosh-area--side" role="img" aria-label="Decorative orange and green curved swooshes"></div>
  <div class="watermark watermark--side" role="img" aria-label="Faint pale yellow gear watermark"></div>

  <section class="details">
    <div class="details__block">WHO:<br>Led by Maren Holtby,<br>Cognitive Speech Therapist</div>
    <div class="details__block">WHERE:<br>4971 E Pruett Ave<br>Kennewick, WA 99336</div>
    <div class="details__block">CONTACT:<br>509-218-3907</div>
  </section>

  <section class="panel">
    <div class="watermark watermark--panel" role="img" aria-label="Faint light blue gear watermark"></div>
    <h1 class="panel__title">ORGANIZATION</h1>
    <div class="panel__art" role="img" aria-label="Illustration of small figures holding hands while stepping up a path of puzzle pieces"></div>
    <ul class="benefits">
      <li><svg class="gear" aria-hidden="true"><use href="#gear-icon"/></svg>Write out your goals for the year.</li>
      <li><svg class="gear" aria-hidden="true"><use href="#gear-icon"/></svg>How to organize your life in 3 easy steps.</li>
      <li><svg class="gear" aria-hidden="true"><use href="#gear-icon"/></svg>Have fun organizing your life and plans.</li>
      <li><svg class="gear" aria-hidden="true"><use href="#gear-icon"/></svg>Join a group of people dedicated to organizing all areas of life.</li>
      <li><svg class="gear" aria-hidden="true"><use href="#gear-icon"/></svg>Complete your tasks in a fast, fun game format.</li>
      <li><svg class="gear" aria-hidden="true"><use href="#gear-icon"/></svg>Walk away with your major goals broken down into their<br>component parts and organize on a yearly calendar.</li>
      <li><svg class="gear" aria-hidden="true"><use href="#gear-icon"/></svg>Three 3 hour days spent in making your life happier, less stressed<br>and with realistic picture of what needs to be accomplished.</li>
      <li><svg class="gear" aria-hidden="true"><use href="#gear-icon"/></svg>More effective in everything I do.<br>Being organized helps free our minds, enjoy relationships more,<br>feel happier, and have greater meaning in life.</li>
    </ul>
  </section>

  <footer class="band">
    <p class="band__text">YOU WILL WALK AWAY WITH DETAILED PLANS FOR 2013.</p>
  </footer>

  <div class="price-badge">
    <svg viewBox="0 0 160 150" width="160" height="150" aria-hidden="true">
      <defs>
        <radialGradient id="badgeFill" cx="50%" cy="45%" r="60%">
          <stop offset="0%" stop-color="#fff27a"/>
          <stop offset="100%" stop-color="var(--badge)"/>
        </radialGradient>
      </defs>
      <polygon fill="url(#badgeFill)" stroke="var(--badge-edge)" stroke-width="2"
        points="80,4 93,20 112,10 117,31 138,30 134,51 154,60 139,75 154,90 134,99 138,120 117,119 112,140 93,130 80,146 67,130 48,140 43,119 22,120 26,99 6,90 21,75 6,60 26,51 22,30 43,31 48,10 67,20"/>
    </svg>
    <div class="price-badge__text">ONLY<br>$600<br>FOR ALL<br>3 DAYS</div>
  </div>
</main>
</body>
</html>
```